Northern Tempest Informational Sheet

I need a one page informational sheet (advertisement) for a horse called Northern Tempest. It should have the name Northern Tempest and the content below. It needs to be eye-catching. I have attached 3 examples of what these advertisements look like so it's easier to create. I've also attached 2 pictures of the horse which should both be used in the advertisement.

Here are the bullet points:

- Son of Distant Harbor with total progeny earnings over 13 million dollars
- Ranks among West Virginia top 3 active sires by progeny earnings 2019
- In 9 crops of racing age, has sired 200 winners from 275 starters
- Sired Don Marbellino who earned over $800k racing from age 2 to 7.
- Won 3 of 4 lifetime starts

stands at stud for $1000 at Ashgrove Farm near Charles Town
Call Dwight Kessler - (304) 555-0193

Target Market(s)

Thoroughbred racing people interested in breeding

Requirements
Must have
• Unique and creative. The name of the horse Northern Tempest should be clear and bold, the picture should also be prominent.
Should not have
• Cartoon like, whimsical

```html
<!DOCTYPE html>
<html lang="en">
<head>
<meta charset="utf-8">
<title>Northern Tempest – Stallion Sheet</title>
<link rel="stylesheet" href="https://fonts.googleapis.com/css2?family=Montserrat:wght@800;900&family=Open+Sans:wght@400;600;700&display=swap">
<style>
  :root{
    --wood-dark:#3b2414;
    --wood-mid:#6b4326;
    --wood-light:#8e6038;
    --paper:#f3eee6;
    --paper-edge:#d9cfc0;
    --ink:#2a2320;
    --accent:#c3241c;
    --bar:#5a3619;
    --bar-text:#f6eadb;
    --price:#ffb23a;
    --title:#ffffff;
    --page:#dcdcdc;
  }
  *{margin:0;padding:0;box-sizing:border-box}
  html,body{width:683px;height:1200px;overflow:hidden;background:var(--page)}
  .sheet{
    position:relative;width:683px;height:1200px;overflow:hidden;
    background:
      radial-gradient(ellipse at 50% 40%, rgba(255,255,255,.08), rgba(0,0,0,.35) 85%),
      linear-gradient(180deg,var(--wood-mid),var(--wood-light) 45%,var(--wood-mid) 75%,var(--wood-dark));
    font-family:"Open Sans",Arial,sans-serif;
  }
  .sheet__title{
    position:absolute;top:58px;left:0;right:0;text-align:center;
    font-family:"Montserrat",Arial,sans-serif;font-weight:900;
    color:var(--title);font-size:74px;line-height:.98;letter-spacing:1px;
    text-transform:uppercase;text-shadow:0 4px 10px rgba(0,0,0,.55);
  }
  .sheet__photo{
    position:absolute;top:262px;left:30px;width:623px;height:450px;
  }
  .sheet__photo svg{display:block;width:100%;height:100%}
  .facts{
    position:absolute;top:690px;left:40px;width:603px;height:360px;
  }
  .facts__paper{position:absolute;inset:0}
  .facts__list{
    position:relative;list-style:none;padding:58px 54px 0 60px;
    color:var(--ink);font-size:17.5px;line-height:1.42;font-weight:600;
  }
  .facts__list li{position:relative;padding-left:20px;margin-bottom:11px}
  .facts__list li::before{
    content:"";position:absolute;left:0;top:10px;width:7px;height:7px;border-radius:50%;background:var(--ink);
  }
  .facts__list em{font-style:normal;color:var(--accent);font-weight:700}
  .stud-bar{
    position:absolute;top:1066px;left:62px;width:559px;height:82px;
    background:var(--bar);border:2px solid rgba(255,255,255,.25);
    box-shadow:0 4px 10px rgba(0,0,0,.45);
    display:flex;flex-direction:column;justify-content:center;align-items:center;
    color:var(--bar-text);font-size:17px;font-weight:600;line-height:1.45;text-align:center;
  }
  .stud-bar strong{color:var(--price);font-weight:700}
</style>
</head>
<body>
<main class="sheet">
  <h1 class="sheet__title">Northern<br>Tempest</h1>

  <div class="sheet__photo">
    <svg viewBox="0 0 623 450" role="img" aria-label="Photograph of the bay stallion Northern Tempest standing in profile on a paved yard beside a brick barn">
      <defs>
        <linearGradient id="photoTone" x1="0" y1="0" x2="0" y2="1">
          <stop offset="0" stop-color="#c9d2da"/>
          <stop offset=".45" stop-color="#8c7a68"/>
          <stop offset=".7" stop-color="#6d5140"/>
          <stop offset="1" stop-color="#5f6670"/>
        </linearGradient>
      </defs>
      <polygon fill="url(#photoTone)" points="14,10 60,2 120,14 190,4 260,16 330,6 400,18 470,4 540,14 610,6 620,60 612,130 622,200 610,270 620,340 608,400 616,444 540,436 470,448 400,438 330,448 260,436 190,446 120,438 60,448 4,440 12,370 2,300 14,230 4,160 14,90"/>
    </svg>
  </div>

  <section class="facts">
    <svg class="facts__paper" viewBox="0 0 603 360" preserveAspectRatio="none" aria-hidden="true">
      <polygon fill="var(--paper-edge)" points="0,30 40,10 90,34 150,8 210,28 270,6 330,30 390,10 450,32 510,8 560,26 603,12 596,120 603,240 594,350 520,340 450,358 380,344 300,360 220,342 150,356 80,340 8,354 2,240 10,120"/>
      <polygon fill="var(--paper)" points="8,36 44,18 92,40 152,16 212,34 272,14 332,36 392,16 452,38 510,16 560,32 595,20 588,120 595,240 586,342 520,332 450,350 380,336 300,352 220,334 150,348 80,332 16,346 10,240 18,120"/>
    </svg>
    <ul class="facts__list">
      <li>Son of Distant Harbor with total progeny earnings <em>over 13 million dollars</em></li>
      <li>Ranks among West Virginia <em>top 3 active sires</em> by progeny earnings 2019</li>
      <li>In 9 crops of racing age, has sired <em>200 winners from 275 starters</em></li>
      <li>Sired Don Marbellino who earned <em>over $800k racing from age 2 to 7</em></li>
      <li><em>Won 3 of 4 lifetime starts</em></li>
    </ul>
  </section>

  <footer class="stud-bar">
    <p>Stands at stud for <strong>$1000</strong> at Ashgrove Farm near Charles Town</p>
    <p>Call Dwight Kessler - (304) 555-0193</p>
  </footer>
</main>
</body>
</html>
```